Waste Oil Filter collection & disposal

Basically I need a 1 page website for the business called Brenmoor Waste Solutions.
We are a environmental service provider and we collect and dispose of waste oil filters to protect the environment from hazardous waste oil products.

This is the link to our current website: www.brenmoorwaste.co.nz

we want it to look fresh and better than our current website. we may potentially look at getting a new logo designed and are open to ideas/designs if you have any.

Industry/Entity Type

Business

Logo Text

Brenmoor Waste Solutions

Number of Pages Required

1 page

Requirements
Must have
• same colours as current website.
• description of what service we provide please refer to leaflet attached

```html
<!DOCTYPE html>
<html lang="en">
<head>
<meta charset="utf-8">
<title>Brenmoor Waste Solutions</title>
<link href="https://fonts.googleapis.com/css2?family=Oswald:wght@400;500&family=Open+Sans:wght@400&family=Roboto:wght@300;400;500;700&display=swap" rel="stylesheet">
<style>
:root{
  --green:#5c9f33;
  --green-light:#6cae3f;
  --green-dark:#4b8a27;
  --ink:#222;
  --text:#555;
  --muted:#888;
  --grey-bg:#f1f1f1;
  --footer:#1c1c1c;
  --white:#fff;
}
*{box-sizing:border-box;margin:0;padding:0}
html,body{width:1200px;height:2961px;overflow:hidden;background:var(--white)}
body{font-family:'Roboto',Arial,sans-serif;color:var(--text)}
.page{position:relative;width:1200px;height:2961px;overflow:hidden}
.abs{position:absolute}

/* header */
.site-header{position:absolute;left:0;top:0;width:1200px;height:112px;background:var(--white)}
.brand{position:absolute;left:95px;top:30px;display:flex;align-items:center;gap:10px}
.brand-dot{width:26px;height:26px;border-radius:50%;background:var(--green)}
.brand-name{font-family:'Roboto',sans-serif;font-weight:700;font-size:15px;color:var(--ink);line-height:1.1;width:150px;text-transform:uppercase}
.brand-tag{position:absolute;left:131px;top:76px;font-size:10px;font-style:italic;color:var(--muted)}
.nav a{position:absolute;top:45px;font-size:16px;color:#333;text-decoration:none;text-transform:uppercase;letter-spacing:.2px}
.nav a.active{color:var(--green-light)}
.nav-divider{position:absolute;left:1046px;top:30px;width:2px;height:44px;background:#bbb}

/* hero */
.hero{position:absolute;left:0;top:112px;width:1200px;height:559px;background:linear-gradient(115deg,#1d3f6a 0%,#2f5f8f 35%,#3b6f86 60%,#5d7a78 80%,#8a8c82 100%)}
.hero-title{position:absolute;right:88px;top:218px;font-family:'Oswald',sans-serif;font-weight:500;font-size:58px;color:var(--white);letter-spacing:-.5px;line-height:1}
.hero-sub{position:absolute;right:88px;top:284px;font-family:'Open Sans',sans-serif;font-size:28px;color:var(--white)}
.hero-wave{position:absolute;left:0;top:0}

/* about */
.section-title{font-family:'Roboto',sans-serif;font-weight:400;color:var(--ink);text-transform:uppercase}
.about-title{left:91px;top:772px;font-size:30px}
.body-text{font-size:13px;line-height:23px;color:var(--text);text-align:justify}
.about-text{left:91px;top:818px;width:549px}
.btn{position:absolute;display:flex;align-items:center;justify-content:center;background:var(--green);color:var(--white);border-radius:18px;font-size:12px;text-transform:uppercase;box-shadow:0 0 0 3px #d9ead0}
.about-btn{left:91px;top:979px;width:99px;height:32px}
.video-frame{left:697px;top:754px;width:416px;height:265px;background:var(--white);box-shadow:0 1px 6px rgba(0,0,0,.35);padding:6px}
.video-fill{width:100%;height:100%;background:linear-gradient(180deg,#3d5b3a 0%,#b8c3bd 45%,#7e8f86 75%,#4a5a47 100%)}
.play{position:absolute;left:874px;top:856px;width:60px;height:60px;border-radius:50%;background:rgba(60,60,60,.6)}

/* services */
.services-band{left:0;top:1111px;width:1200px;height:257px;background:var(--green)}
.services-title{left:0;top:1170px;width:1200px;text-align:center;font-size:32px;color:var(--white)}
.service{position:absolute;width:300px;text-align:center}
.service-img{width:182px;height:182px;margin:0 auto;border-radius:50%;border:4px solid var(--white);box-shadow:0 2px 6px rgba(0,0,0,.3)}
.service h3{font-weight:400;font-size:26px;color:var(--ink);margin-top:22px}
.service p{font-size:14px;line-height:22px;color:#444;margin-top:12px;padding:0 12px}
.service .more{font-size:14px;color:var(--green-light);margin-top:9px}

/* what we do */
.wwd-back{left:142px;top:1717px;width:326px;height:300px;background:var(--green)}
.wwd-img{left:162px;top:1737px;width:326px;height:302px;background:linear-gradient(135deg,#6b7769 0%,#2e7c5c 40%,#1f6b4c 65%,#a89a7a 100%);box-shadow:0 4px 12px rgba(0,0,0,.4)}
.wwd-title{left:541px;top:1762px;font-size:32px}
.wwd-text{left:541px;top:1812px;width:515px}
.wwd-btn{left:541px;top:1978px;width:116px;height:36px;font-size:13px}

/* blog & reviews */
.grey{left:0;top:2138px;width:1200px;height:520px;background:var(--grey-bg)}
.blog-title{left:97px;top:2240px;font-size:24px}
.post{position:absolute;left:97px;width:600px;height:116px}
.post-img{position:absolute;left:0;top:0;width:183px;height:116px;border:3px solid var(--white);box-shadow:0 1px 4px rgba(0,0,0,.25)}
.post h4{position:absolute;left:207px;top:6px;font-weight:500;font-size:17px;color:#333}
.post .date{position:absolute;left:207px;top:32px;font-size:11px;color:#333;text-transform:uppercase}
.post .excerpt{position:absolute;left:207px;top:52px;width:360px;font-size:13px;line-height:20px;color:#555;font-weight:500}
.post .more{position:absolute;left:207px;top:97px;font-size:11px;color:var(--green)}
.reviews-title{left:770px;top:2240px;font-size:24px}
.quote-box{left:774px;top:2290px;width:333px;height:154px;background:var(--green);color:var(--white);padding:28px 28px;font-size:13px;line-height:24px;text-align:justify}
.quote-box .q{font-size:30px;font-family:Georgia,serif;font-weight:700;line-height:0;vertical-align:-10px}
.avatar{left:793px;top:2463px;width:80px;height:80px;border-radius:50%;background:radial-gradient(circle at 50% 45%,#d8c6b8 0%,#8d7a6e 60%,#3a3634 100%)}
.reviewer{left:892px;top:2470px;font-size:16px;color:#333}
.arrow-btn{position:absolute;top:2515px;width:20px;height:20px;border:1px solid #ccc;border-radius:3px;background:var(--white)}

/* footer */
.footer{left:0;top:2600px;width:1200px;height:361px}
.f-brand{left:97px;top:2765px;display:flex;align-items:center;gap:10px}
.f-brand .brand-name{color:var(--white);font-size:14px}
.f-head{position:absolute;top:2724px;font-size:15px;color:var(--white)}
.f-text{position:absolute;font-size:11px;line-height:21.5px;color:#ddd}
.input{left:667px;top:2803px;width:146px;height:28px;background:var(--white);font-size:11px;color:#777;padding:7px 10px}
.submit{left:813px;top:2803px;width:56px;height:28px;background:var(--green);color:var(--white);font-size:11px;text-align:center;padding-top:7px}
.social{position:absolute;top:2763px;width:26px;height:26px;border-radius:4px;background:var(--white)}
.f-rule{left:97px;top:2878px;width:1006px;height:1px;background:#3a3a3a}
.copyright{left:0;top:2912px;width:1200px;text-align:center;font-size:14px;color:#ddd}
</style>
</head>
<body>
<div class="page">

  <header class="site-header">
    <div class="brand"><span class="brand-dot"></span><span class="brand-name">Brenmoor Waste Solutions Ltd</span></div>
    <div class="brand-tag">Our aim is to keep NZ Green</div>
    <nav class="nav">
      <a class="active" style="left:409px">Home</a>
      <a style="left:497px">Services</a>
      <a style="left:614px">About Us</a>
      <a style="left:736px">Blog</a>
      <a style="left:815px">My Gallery</a>
      <a style="left:947px">Contact</a>
    </nav>
    <div class="nav-divider"></div>
    <svg class="abs" style="left:1071px;top:46px" width="20" height="20" viewBox="0 0 20 20"><circle cx="8" cy="8" r="6" fill="none" stroke="#222" stroke-width="2.5"/><line x1="12.5" y1="12.5" x2="18" y2="18" stroke="#222" stroke-width="3" stroke-linecap="round"/></svg>
  </header>

  <section class="hero" role="img" aria-label="Stacked blue and green oil drums">
    <h1 class="hero-title">BRENMOOR WASTE SOLUTIONS</h1>
    <p class="hero-sub">Oil Filter Collection &amp; Disposal Service</p>
    <svg class="abs" style="left:1060px;top:418px" width="48" height="18" viewBox="0 0 48 18">
      <path d="M11 3 L5 9 L11 15" fill="none" stroke="#fff" stroke-width="2.5"/>
      <path d="M37 3 L43 9 L37 15" fill="none" stroke="#fff" stroke-width="2.5"/>
    </svg>
  </section>
  <svg class="hero-wave" width="1200" height="700" viewBox="0 0 1200 700">
    <path d="M0,661 C300,655 600,582 870,586 C1000,590 1120,612 1200,630 L1200,700 L0,700 Z" fill="#fff"/>
    <path d="M0,661 C300,655 600,582 870,586 C1000,590 1120,612 1200,630" fill="none" stroke="#5c9f33" stroke-width="5"/>
  </svg>

  <h2 class="section-title abs about-title">About Us</h2>
  <p class="body-text abs about-text">&nbsp;Lorem Ipsum has been the industry's standard dummy text ever since the 1500s, when an unknown printer took a galley of type and scrambled it to make a type specimen book. It has survived not only five centuries, but also the leap into electronic typesetting, remaining essentially unchanged. It was popularised in the 1960s with the release of Letraset sheets containing Lorem Ipsum passages, and more recently with desktop publishing software like Aldus PageMaker including versions of Lorem Ipsum</p>
  <div class="btn about-btn">Read More</div>
  <div class="abs video-frame"><div class="video-fill" role="img" aria-label="Video still of a green and white filter collection truck"></div></div>
  <svg class="abs" style="left:874px;top:856px" width="60" height="60" viewBox="0 0 60 60"><circle cx="30" cy="30" r="30" fill="rgba(50,50,50,.6)"/><path d="M24 18 L42 30 L24 42 Z" fill="#fff"/></svg>

  <div class="abs services-band"></div>
  <h2 class="section-title abs services-title">Our Services</h2>
  <div class="service" style="left:109px;top:1267px">
    <div class="service-img" role="img" aria-label="Filter processing machinery" style="background:linear-gradient(135deg,#5d6660,#9aa19c 50%,#3b3f3d)"></div>
    <h3>Filter processing</h3>
    <p>It has survived not only five centuries, but also the leap into electronic</p>
    <div class="more">Read More -&gt;</div>
  </div>
  <div class="service" style="left:450px;top:1267px">
    <div class="service-img" role="img" aria-label="Compressed brick of used oil filters" style="background:linear-gradient(135deg,#2a2f3a,#6b7080 50%,#24262c)"></div>
    <h3>Brick of filters</h3>
    <p>It has survived not only five centuries, but also the leap into electronic</p>
    <div class="more">Read More -&gt;</div>
  </div>
  <div class="service" style="left:794px;top:1267px">
    <div class="service-img" role="img" aria-label="Filter bailer in a workshop" style="background:linear-gradient(135deg,#5f7a72,#9fb0a8 50%,#2b3d3a)"></div>
    <h3>Filter Bailer</h3>
    <p>It has survived not only five centuries, but also the leap into electronic</p>
    <div class="more">Read More -&gt;</div>
  </div>

  <div class="abs wwd-back"></div>
  <div class="abs wwd-img" role="img" aria-label="Green filter crushing press in a shed"></div>
  <h2 class="section-title abs wwd-title">What We Do</h2>
  <p class="body-text abs wwd-text">Lorem Ipsum has been the industry's standard dummy text ever since the 1500s, when an unknown printer took a galley of type and scrambled it to make a type specimen book. It has survived not only five centuries, but also the leap into electronic typesetting, remaining essentially unchanged. It was popularised in the 1960s with the release of Letraset sheets containing Lorem Ipsum passages, and more recently with desktop publishing software like Aldus PageMaker.</p>
  <div class="btn wwd-btn">Read More</div>

  <div class="abs grey"></div>
  <h2 class="section-title abs blog-title">Latest Blog</h2>
  <article class="post" style="top:2290px">
    <div class="post-img" role="img" aria-label="Pile of used oil filters" style="background:linear-gradient(135deg,#4a4f58,#8d9098 50%,#33363c)"></div>
    <h4>Nemo Enim Ipsam Voluptatem</h4>
    <div class="date">July 20, 2017</div>
    <p class="excerpt">Lorem ipsum dolor sit amet, consectetur adipiscing elit, sed do eiusmod tempor incididunt ut labore</p>
    <div class="more">Read More »</div>
  </article>
  <article class="post" style="top:2430px">
    <div class="post-img" role="img" aria-label="Rows of blue and green drums" style="background:linear-gradient(135deg,#1f4f8a,#3f7fb8 50%,#3c8f6a)"></div>
    <h4>Nemo Enim Ipsam Voluptatem</h4>
    <div class="date">July 20, 2017</div>
    <p class="excerpt">Lorem ipsum dolor sit amet, consectetur adipiscing elit, sed do eiusmod tempor incididunt ut labore</p>
    <div class="more">Read More »</div>
  </article>

  <h2 class="section-title abs reviews-title">Reviews</h2>
  <blockquote class="abs quote-box"><span class="q">“</span> Lorem Ipsum has been the industry's standard dummy text ever since the 1500s, when an unknown printer took a galley of type and scrambled it to make a type specimen <span class="q">”</span></blockquote>
  <div class="abs avatar" role="img" aria-label="Portrait of the reviewer"></div>
  <div class="abs reviewer">Mara Ellison - Manager</div>
  <svg class="arrow-btn" style="left:894px" viewBox="0 0 20 20"><path d="M12 6 L8 10 L12 14" fill="none" stroke="#555" stroke-width="1.5"/></svg>
  <svg class="arrow-btn" style="left:920px" viewBox="0 0 20 20"><path d="M8 6 L12 10 L8 14" fill="none" stroke="#555" stroke-width="1.5"/></svg>

  <svg class="abs footer" width="1200" height="361" viewBox="0 0 1200 361">
    <path d="M0,45 C300,30 650,75 1200,20 L1200,361 L0,361 Z" fill="#1c1c1c"/>
  </svg>
  <div class="abs f-brand"><span class="brand-dot"></span><span class="brand-name">Brenmoor Waste Solutions Ltd</span></div>

  <div class="f-head" style="left:349px">Contact us</div>
  <div class="f-text" style="left:349px;top:2762px">Address : Unit 12, Harrow Lane Business<br>Park 4, Kelvale, Northbrook<br>Phone : 06 417 2285<br>Email : hello@brenmoorwaste.co.nz</div>

  <div class="f-head" style="left:667px">Sign up for newsletter</div>
  <div class="f-text" style="left:667px;top:2755px;width:210px;line-height:17px">Your about us information would fit here nicely.</div>
  <div class="abs input">Email address</div>
  <div class="abs submit">Submit</div>

  <div class="f-head" style="left:973px">Follow us out there</div>
  <div class="social" style="left:973px" role="img" aria-label="Social profile"></div>
  <div class="social" style="left:1010px" role="img" aria-label="Social profile"></div>
  <div class="social" style="left:1048px" role="img" aria-label="Social profile"></div>
  <div class="social" style="left:1086px" role="img" aria-label="Social profile"></div>

  <div class="abs f-rule"></div>
  <div class="abs copyright">Copyright © 2017. All Rights Reserved</div>
</div>
</body>
</html>
```